quiet meadow therapy (QMT)

I need to build a website for my therapy business.
There are two parts to the website
on the landing page; they choose whether they are therapists making a referral or patients needing more information.
After that, they are taken to their respective pages.
There is the textual information and a referral form on the therapist page, and on the patient page, the text is a bit different, and there will be a booking page on the patient page.
Visually minimal, it's a therapeutic website. I want it clean, clinical, and modern
colors: greenish blue or maybe orangish
PHP/html code
Updates

Hi everyone
I'm very sorry for the lack of responses to your designs. I am trying to work it out, but this platform has been a challenge for me.
I appreciate everyone's efforts, and I am unsure how to rate designs and move forward with the ones I like. There is a 5-star rating, but I don't understand how I'm supposed to politely say that it is not it without feeling like I'm going to affect someone's future rating negatively.
Please understand me. Thank you

Designs look the same

Target Market(s)

therapy and stress management

Industry/Entity Type

stress management therapy

Coding

Coded - Design and coding required

Number of Pages Required

5+ page

Font styles to use
Serif

Colors
0094D4
00A9DD
6FCCEA
C7EBF8
E9F6FB
00AB8E
00BBA5
67D7C9
C6EFE9
E9F9F6

Requirements
Must have
• landing page that that have 2 options. one for therapist another for patient

```html
<!DOCTYPE html>
<html lang="en">
<head>
<meta charset="utf-8">
<title>Quiet Meadow Therapy – Website Screens</title>
<link href="https://fonts.googleapis.com/css2?family=Cinzel:wght@500;600&family=Montserrat:ital,wght@0,400;0,500;0,600;1,400&display=swap" rel="stylesheet">
<style>
  :root{
    --canvas:#f2f2f2;
    --white:#ffffff;
    --ink:#1d1d1d;
    --text:#555555;
    --muted:#777777;
    --orange:#f7941d;
    --orange-soft:#f9b25a;
    --teal:#16a595;
    --teal-bright:#2cc0ad;
    --teal-soft:#8fd4cb;
    --teal-pale:#cfeae6;
    --mist:#eef6f5;
    --rule:#bdbdbd;
    --bar:#231f20;
    --circle:#f1f1f1;
  }
  *{box-sizing:border-box;margin:0;padding:0}
  html,body{width:1200px;height:992px;overflow:hidden;background:var(--canvas)}
  body{font-family:"Montserrat",Arial,sans-serif;color:var(--ink)}
  .board{position:absolute;left:0;top:0;width:2100px;height:1736px;transform:scale(0.5714286);transform-origin:0 0}
  .abs{position:absolute}
  .serif{font-family:"Cinzel",Georgia,serif;font-weight:500}

  .btn{position:absolute;display:flex;align-items:center;justify-content:center;background:var(--orange);color:var(--white);border-radius:20px;font-size:11px;font-weight:500;letter-spacing:.3px}
  .brand{position:absolute;display:flex;align-items:center;gap:10px}
  .brand-dot{border-radius:50%;background:var(--teal)}
  .brand-name{font-family:"Montserrat",Arial,sans-serif;font-weight:500;color:var(--ink)}
  .photo{position:absolute}

  /* landing card */
  .landing{left:86px;top:146px;width:588px;height:401px;background:var(--bar);box-shadow:0 6px 18px rgba(0,0,0,.12);overflow:hidden}
  .landing .half{position:absolute;top:0;width:294px;height:354px}
  .landing .half.therapists{left:0;background:linear-gradient(160deg,#d8d3cc 0%,#a79a8c 45%,#4e463f 100%)}
  .landing .half.patients{left:294px;background:linear-gradient(200deg,#7b6d62 0%,#8b8e96 40%,#3e4452 100%)}
  .landing .half h2{position:absolute;left:0;right:0;top:216px;text-align:center;color:var(--white);font-size:21px;font-weight:500}
  .landing .half p{position:absolute;left:50px;right:50px;top:250px;text-align:center;color:#eeeeee;font-size:9.5px;line-height:14px}
  .landing .half .btn{left:96px;top:290px;width:103px;height:34px;font-size:11px}
  .landing .veil{position:absolute;border-radius:50%;background:rgba(255,255,255,.86);width:130px;height:130px;top:26px}
  .landing .copyright{position:absolute;left:0;right:0;top:354px;height:47px;display:flex;align-items:center;justify-content:center;color:#eee;font-size:8.5px}

  /* web pages */
  .page{position:absolute;top:105px;width:588px;background:var(--white);overflow:hidden}
  .page.home{left:756px;height:1472px}
  .page.therapist{left:1426px;height:1527px}
  .site-header{position:absolute;left:0;top:0;width:588px;height:58px;background:var(--white)}
  .site-nav{position:absolute;top:22px;left:0;width:588px;font-size:9px;font-weight:500;color:var(--ink)}
  .site-nav span{position:absolute;top:2px}
  .site-nav .current{color:var(--orange)}
  .site-nav .signup{position:absolute;left:480px;top:-4px;width:54px;height:25px;border-radius:13px;background:var(--orange);color:var(--white);display:flex;align-items:center;justify-content:center;font-size:8.5px}

  .section{position:absolute;left:0;width:588px}
  .center{text-align:center;left:0;right:0}
  .heading{font-size:19px;letter-spacing:.4px;color:var(--ink)}
  .body-text{font-size:8.5px;line-height:13.8px;color:var(--text)}

  /* home hero */
  .hero-photo{left:0;top:0;width:588px;height:486px;background:linear-gradient(135deg,#6a4a3a 0%,#3c3b3f 35%,#5e6a72 60%,#c9c3bc 80%,#8a6f5d 100%)}
  .hero-photo::after{content:"";position:absolute;inset:0;background:rgba(20,20,25,.35)}
  .hero-title{top:64px;font-size:31px;color:var(--white);letter-spacing:.5px}
  .outline-btn{position:absolute;left:244px;top:118px;width:100px;height:30px;border:1.5px solid var(--white);border-radius:16px;color:var(--white);font-size:9px;font-weight:500;display:flex;align-items:center;justify-content:center}
  .choice-icon{position:absolute;width:52px;height:54px;border-radius:50%;background:radial-gradient(circle at 50% 42%,var(--orange-soft) 0%,var(--teal-bright) 30%,var(--teal) 52%,var(--teal-pale) 78%,var(--white) 100%)}
  .choice h3{position:absolute;top:341px;font-size:19px;text-align:center;width:230px}
  .choice p{position:absolute;top:374px;width:190px;text-align:center;font-size:9px;line-height:14px;color:var(--text)}

  /* welcome */
  .welcome{top:543px;height:275px;background:var(--mist)}
  .welcome h2{position:absolute;left:54px;top:34px;font-size:19px;line-height:24px;color:var(--ink)}
  .welcome p{position:absolute;left:54px;top:116px;width:222px}
  .video{left:294px;top:33px;width:240px;height:154px;background:linear-gradient(120deg,#e9e5df 0%,#b9b1a6 40%,#6d7d8d 70%,#c0b4a6 100%)}
  .play{position:absolute;left:106px;top:63px;width:28px;height:28px;border-radius:50%;background:#111;display:flex;align-items:center;justify-content:center}

  /* services */
  .services{top:818px;height:236px;background:var(--white)}
  .service{position:absolute;top:66px;width:120px;text-align:center}
  .service .disc{width:110px;height:110px;border-radius:50%;margin:0 auto;background:radial-gradient(circle at 50% 42%,var(--orange-soft) 0%,var(--orange) 16%,var(--teal-bright) 34%,var(--teal) 50%,var(--teal-pale) 66%,var(--circle) 82%)}
  .service .disc.calm{background:radial-gradient(circle at 50% 45%,var(--orange) 0%,var(--teal) 28%,var(--teal-bright) 48%,var(--teal-pale) 66%,var(--circle) 82%)}
  .service .disc.pair{background:radial-gradient(ellipse 60% 50% at 50% 50%,var(--orange-soft) 0%,var(--teal-bright) 36%,var(--teal) 52%,var(--teal-pale) 70%,var(--circle) 86%)}
  .service .disc.split{background:radial-gradient(circle at 50% 50%,var(--teal) 0%,var(--orange) 26%,var(--teal-bright) 46%,var(--teal-pale) 66%,var(--circle) 82%)}
  .service span{display:block;margin-top:15px;font-size:11px;font-weight:500;color:var(--ink)}
  .chev{position:absolute;font-size:20px;line-height:1;color:#555}

  /* testimonials */
  .testimonials{height:224px;background:linear-gradient(120deg,#2bbfac 0%,#14a290 45%,#1a9a8c 70%,#13a391 100%);overflow:hidden}
  .testimonials .title{top:26px;font-size:20px;color:var(--white)}
  .quote-card{position:absolute;top:67px;width:150px;height:111px;background:var(--white);text-align:center;padding-top:12px}
  .quote-card.featured{background:var(--orange);height:124px}
  .stars{font-size:9px;letter-spacing:1px;color:var(--orange)}
  .featured .stars{color:var(--white)}
  .quote-card q{display:block;margin:8px 12px 0;font-size:8px;line-height:13px;font-style:italic;color:#666}
  .featured q{color:var(--white)}
  .quote-card .who{display:block;margin-top:8px;font-size:9px;font-weight:500;color:var(--ink)}
  .featured .who{color:var(--white)}
  .testimonials .chev{color:var(--white);top:108px}

  /* footer */
  .site-footer{height:150px;background:var(--white)}
  .social{position:absolute;top:104px;width:21px;height:21px;border:1px solid #9a9a9a;border-radius:50%}
  .foot-col{position:absolute;top:30px;font-size:8px;color:var(--text)}
  .foot-col h4{font-size:9px;font-weight:500;color:var(--ink);margin-bottom:8px}
  .foot-col li{list-style:none;line-height:15px}
  .contact-line{display:flex;gap:5px;align-items:flex-start;line-height:12px;margin-bottom:12px;width:160px}
  .contact-line svg{flex:none;margin-top:2px}
  .copy-bar{height:44px;background:var(--bar);display:flex;align-items:center;justify-content:center;color:#eee;font-size:8.5px}

  /* therapist page */
  .inner-hero{left:0;top:58px;width:588px;height:179px;background:linear-gradient(110deg,#e7e3dc 0%,#c7bfb3 35%,#8c8a88 55%,#d8c9a9 80%,#efe7da 100%)}
  .inner-hero::after{content:"";position:absolute;inset:0;background:rgba(40,40,40,.18)}
  .inner-hero h1{position:absolute;left:0;right:0;top:68px;text-align:center;color:var(--white);font-size:35px;letter-spacing:.5px;z-index:1}
  .intro p{position:absolute;left:88px;width:412px;top:71px;text-align:center}
  .form-area{top:407px;height:701px;background:var(--mist)}
  .form-card{position:absolute;left:62px;top:69px;width:464px;height:592px;background:var(--white);box-shadow:0 2px 8px rgba(0,0,0,.06);border-radius:3px;font-size:8px;color:var(--ink)}
  .label{position:absolute;text-align:right;white-space:nowrap}
  .line{position:absolute;height:1px;background:var(--rule)}
  .check{display:inline-block;width:8px;height:8px;border:1px solid #777;border-radius:1px;vertical-align:-1px;margin-right:2px}
  .opts{position:absolute;left:238px;color:#555}
  .band{position:absolute;left:0;width:464px;height:28px;background:var(--teal-soft);color:var(--white);font-size:9.5px;font-weight:500;display:flex;align-items:center;justify-content:center;letter-spacing:.2px}
</style>
</head>
<body>
<div class="board">

  <!-- Landing chooser -->
  <section class="abs landing">
    <div class="half therapists" role="img" aria-label="Photo of a smiling therapist with glasses in an office">
      <h2>FOR THERAPISTS</h2>
      <p>Duis aute irure dolor in reprehenderit in voluptate velit esse cillum do.</p>
      <div class="btn">CLICK HERE</div>
    </div>
    <div class="half patients" role="img" aria-label="Photo of a smiling young patient during a session">
      <h2>FOR PATIENTS</h2>
      <p>Duis aute irure dolor in reprehenderit in voluptate velit esse cillum do.</p>
      <div class="btn">CLICK HERE</div>
    </div>
    <div class="veil" style="left:201px"></div>
    <div class="veil" style="left:259px"></div>
    <div class="brand" style="left:222px;top:68px">
      <span class="brand-dot" style="width:26px;height:26px"></span>
      <span class="brand-name" style="font-size:36px;letter-spacing:9px">QMT</span>
    </div>
    <div class="copyright">Copyright © 2022, Quiet Meadow Therapy. All rights reserved.</div>
  </section>

  <!-- Home page -->
  <main class="page home">
    <section class="section" style="top:58px;height:485px;overflow:hidden">
      <div class="photo hero-photo" role="img" aria-label="Photo of a therapist taking notes on a notepad during a session"></div>
      <h1 class="abs center serif hero-title">QUIET MEADOW THERAPY</h1>
      <div class="outline-btn">GET MORE INFO</div>
      <svg class="abs" style="left:0;top:0" width="588" height="485" viewBox="0 0 588 485" aria-hidden="true">
        <circle cx="260" cy="529" r="285" fill="#ffffff"/>
        <circle cx="328" cy="529" r="285" fill="#ffffff"/>
        <circle cx="260" cy="529" r="285" fill="none" stroke="#ececec" stroke-width="1"/>
        <circle cx="328" cy="529" r="285" fill="none" stroke="#ececec" stroke-width="1"/>
      </svg>
      <div class="choice">
        <div class="choice-icon" role="img" aria-label="Teal and orange line icon of a head with a thought" style="left:151px;top:273px"></div>
        <h3 class="serif" style="left:62px">FOR THERAPISTS</h3>
        <p style="left:82px">Duis aute irure dolor in reprehenderit in voluptate velit esse cillum do.</p>
        <div class="btn" style="left:126px;top:417px;width:103px;height:34px">CLICK HERE</div>
      </div>
      <div class="choice">
        <div class="choice-icon" role="img" aria-label="Teal and orange line icon of a person under stress" style="left:380px;top:273px"></div>
        <h3 class="serif" style="left:291px">FOR PATIENTS</h3>
        <p style="left:311px">Duis aute irure dolor in reprehenderit in voluptate velit esse cillum do.</p>
        <div class="btn" style="left:355px;top:417px;width:103px;height:34px">CLICK HERE</div>
      </div>
    </section>

    <header class="site-header">
      <div class="brand" style="left:54px;top:14px">
        <span class="brand-dot" style="width:24px;height:24px"></span>
        <span class="brand-name" style="font-size:26px;letter-spacing:8px">QMT</span>
      </div>
      <nav class="site-nav">
        <span class="current" style="left:233px">HOME</span>
        <span style="left:276px">ABOUT</span>
        <span style="left:324px">SERVICES</span>
        <span style="left:383px">BLOG</span>
        <span style="left:424px">CONTACT</span>
        <span class="signup">SIGN UP</span>
      </nav>
    </header>

    <section class="section welcome">
      <h2 class="serif">WELCOME TO<br>QUIET MEADOW<br>THERAPY</h2>
      <p class="body-text">Nemo enim ipsam voluptatem quia voluptas sit asper natur aut odit aut fugit, sed quia consequuntur magni dolores eos qui ratione voluptatem sequi nesciu leque porro quisquam est, qui dolorem ipsum quia dolor sit amet, consectetur, adipisci velit, sed quia non numiq uam eius modi tempora incidun.</p>
      <div class="btn" style="left:54px;top:212px;width:76px;height:28px;font-size:8.5px">READ MORE</div>
      <div class="photo video" role="img" aria-label="Video still of a patient talking with a therapist">
        <div class="play"><svg width="10" height="10" viewBox="0 0 10 10"><path d="M2 1 L9 5 L2 9 Z" fill="#fff"/></svg></div>
      </div>
    </section>

    <section class="section services">
      <h2 class="abs center serif heading" style="top:32px">SERVICES</h2>
      <span class="chev" style="left:32px;top:110px">‹</span>
      <div class="service" style="left:50px"><div class="disc" role="img" aria-label="Teal and orange illustration of a stressed person"></div><span>Anxiety &amp; Stress</span></div>
      <div class="service" style="left:173px"><div class="disc calm" role="img" aria-label="Teal and orange illustration of a person holding their head"></div><span>Depression</span></div>
      <div class="service" style="left:295px"><div class="disc pair" role="img" aria-label="Teal and orange illustration of two people facing apart"></div><span>Relationship Issues</span></div>
      <div class="service" style="left:418px"><div class="disc split" role="img" aria-label="Teal and orange illustration of a split-tone person"></div><span>Bipolar Disorder</span></div>
      <span class="chev" style="left:546px;top:110px">›</span>
    </section>

    <section class="section testimonials" style="top:1054px">
      <h2 class="abs center serif title">TESTIMONIALS</h2>
      <span class="chev" style="left:28px">‹</span>
      <div class="quote-card" style="left:54px"><div class="stars">★★★★★</div><q>Nemo enim ipsam volupta tem quia voluptas sit asperna tur aut odit aut fugitem quia voluptas sit aspernat</q><span class="who">- John Doe</span></div>
      <div class="quote-card featured" style="left:219px"><div class="stars">★★★★★</div><q>Nemo enim ipsam volupta tem quia voluptas sit asperna tur aut odit aut fugitem quia voluptas sit asperneius modi tempora incidunt ut la</q><span class="who">- John Doe</span></div>
      <div class="quote-card" style="left:384px"><div class="stars">★★★★★</div><q>Nemo enim ipsam volupta tem quia voluptas sit asperna tur aut odit aut fugitem quia voluptas sit aspernat</q><span class="who">- John Doe</span></div>
      <span class="chev" style="left:551px">›</span>
    </section>

    <footer class="section site-footer" style="top:1278px">
      <div class="brand" style="left:54px;top:30px">
        <span class="brand-dot" style="width:40px;height:40px"></span>
        <span class="brand-name" style="font-size:46px;letter-spacing:14px">QMT</span>
      </div>
      <span class="social" style="left:55px"></span>
      <span class="social" style="left:80px"></span>
      <span class="social" style="left:105px"></span>
      <div class="foot-col" style="left:278px"><h4>Quick Links</h4><ul><li>Home</li><li>About</li><li>Services</li><li>Blog</li><li>contact</li></ul></div>
      <div class="foot-col" style="left:370px"><h4>Contact Us</h4>
        <div class="contact-line"><svg width="6" height="8" viewBox="0 0 6 8"><path d="M3 0a3 3 0 0 1 3 3c0 2-3 5-3 5S0 5 0 3a3 3 0 0 1 3-3z" fill="#f7941d"/></svg><span>Nemo enim ipsam voluptatem quia voluptas sit aspernatur</span></div>
        <div class="contact-line"><svg width="8" height="6" viewBox="0 0 8 6"><rect width="8" height="6" fill="#f7941d"/><path d="M0 0 L4 3 L8 0" stroke="#fff" fill="none" stroke-width=".8"/></svg><span>info@quietmeadowtherapy.com</span></div>
        <div class="contact-line"><svg width="7" height="7" viewBox="0 0 7 7"><path d="M1 0 L2.5 0 L3 2 L2 2.8 Q3 4.5 4.2 5 L5 4 L7 4.5 L7 6 Q6.5 7 5.5 7 Q0 6 0 1 Q0 0 1 0z" fill="#f7941d"/></svg><span>+1 888 888 8888</span></div>
      </div>
    </footer>
    <div class="section copy-bar" style="top:1428px">Copyright © 2022, Quiet Meadow Therapy. All rights reserved.</div>
  </main>

  <!-- Therapist page -->
  <main class="page therapist">
    <header class="site-header">
      <div class="brand" style="left:54px;top:14px">
        <span class="brand-dot" style="width:24px;height:24px"></span>
        <span class="brand-name" style="font-size:26px;letter-spacing:8px">QMT</span>
      </div>
      <nav class="site-nav">
        <span class="current" style="left:233px">HOME</span>
        <span style="left:276px">ABOUT</span>
        <span style="left:324px">SERVICES</span>
        <span style="left:383px">BLOG</span>
        <span style="left:424px">CONTACT</span>
        <span class="signup">SIGN UP</span>
      </nav>
    </header>

    <section class="photo inner-hero" role="img" aria-label="Photo of a smiling therapist with glasses in a bright office">
      <h1 class="serif">THERAPISTS</h1>
    </section>

    <section class="section intro" style="top:237px;height:170px">
      <h2 class="abs center serif heading" style="top:36px">THERAPIST REFERRAL</h2>
      <p class="body-text">Nemo enim ipsam voluptatem quia voluptas sit asper natur aut odit aut fugit, sed quia consequuntur magni dolores eos qui ratione voluptatem sequi nesciu leque porro quisquam est, qui dolorem ipsum quia dolor sit amet, consectetur, adipisci velit, sed quia non numiq uam eius. Ut enim ad minima veniam, quis nostrum exercitationem ullam corporis suscipit laboriosam, nisi ut aliquid ex ea commodi cor aut odit aut fugit, sensequatur oluptate velit ess.</p>
    </section>

    <section class="section form-area">
      <h2 class="abs center serif heading" style="top:30px">COUNSELING REFERRAL FORM</h2>
      <form class="form-card">
        <span class="label" style="right:236px;top:29px">Date of Referral:</span>
        <span class="line" style="left:240px;top:36px;width:40px"></span><span class="abs" style="left:283px;top:28px">/</span>
        <span class="line" style="left:290px;top:36px;width:40px"></span><span class="abs" style="left:333px;top:28px">/</span>
        <span class="line" style="left:340px;top:36px;width:40px"></span>
        <span class="abs" style="left:385px;top:29px;font-size:6.5px;color:#555">(MM/DD/YYYY)</span>

        <span class="label" style="right:236px;top:55px">Is client aware of and agreeable to this referral?</span>
        <span class="opts" style="top:54px"><i class="check"></i>Yes &nbsp;<i class="check"></i>No</span>
        <span class="label" style="right:236px;top:76px">Is this referral urgent?</span>
        <span class="opts" style="top:75px"><i class="check"></i>Yes &nbsp;<i class="check"></i>No</span>

        <div class="band" style="top:115px">CLIENT INFORMATION</div>
        <span class="label" style="right:366px;top:164px">Name:</span><span class="line" style="left:106px;top:171px;width:291px"></span>
        <span class="label" style="right:366px;top:190px">Age:</span><span class="line" style="left:106px;top:197px;width:119px"></span>
        <span class="label" style="right:194px;top:190px">Gender:</span><span class="line" style="left:277px;top:197px;width:120px"></span>
        <span class="label" style="right:366px;top:216px">Address:</span><span class="line" style="left:106px;top:223px;width:291px"></span>
        <span class="label" style="right:366px;top:243px">City:</span><span class="line" style="left:106px;top:250px;width:104px"></span>
        <span class="label" style="right:146px;top:243px">Postal Code:</span><span class="line" style="left:325px;top:250px;width:72px"></span>
        <span class="label" style="right:366px;top:270px">Phone No:</span><span class="line" style="left:106px;top:277px;width:291px"></span>
        <span class="label" style="right:366px;top:297px">Email:</span><span class="line" style="left:106px;top:304px;width:291px"></span>

        <div class="band" style="top:333px">REFERRING PROFESSIONAL</div>
        <span class="label" style="right:366px;top:383px">Name:</span><span class="line" style="left:106px;top:390px;width:291px"></span>
        <span class="label" style="right:366px;top:409px">Practice:</span><span class="line" style="left:106px;top:416px;width:291px"></span>
        <span class="label" style="right:366px;top:435px">Address:</span><span class="line" style="left:106px;top:442px;width:291px"></span>
        <span class="label" style="right:366px;top:461px">City:</span><span class="line" style="left:106px;top:468px;width:104px"></span>
        <span class="label" style="right:146px;top:461px">Postal Code:</span><span class="line" style="left:325px;top:468px;width:72px"></span>
        <span class="label" style="right:366px;top:488px">Phone No:</span><span class="line" style="left:106px;top:495px;width:291px"></span>
        <span class="label" style="right:366px;top:515px">Email:</span><span class="line" style="left:106px;top:522px;width:291px"></span>

        <div class="btn" style="left:199px;top:539px;width:66px;height:29px;font-size:8.5px">SUBMIT</div>
      </form>
    </section>

    <section class="section testimonials" style="top:1108px">
      <h2 class="abs center serif title">TESTIMONIALS</h2>
      <span class="chev" style="left:28px">‹</span>
      <div class="quote-card" style="left:54px"><div class="stars">★★★★★</div><q>Nemo enim ipsam volupta tem quia voluptas sit asperna tur aut odit aut fugitem quia voluptas sit aspernat</q><span class="who">- John Doe</span></div>
      <div class="quote-card featured" style="left:219px"><div class="stars">★★★★★</div><q>Nemo enim ipsam volupta tem quia voluptas sit asperna tur aut odit aut fugitem quia voluptas sit asperneius modi tempora incidunt ut la</q><span class="who">- John Doe</span></div>
      <div class="quote-card" style="left:384px"><div class="stars">★★★★★</div><q>Nemo enim ipsam volupta tem quia voluptas sit asperna tur aut odit aut fugitem quia voluptas sit aspernat</q><span class="who">- John Doe</span></div>
      <span class="chev" style="left:551px">›</span>
    </section>

    <footer class="section site-footer" style="top:1332px">
      <div class="brand" style="left:54px;top:30px">
        <span class="brand-dot" style="width:40px;height:40px"></span>
        <span class="brand-name" style="font-size:46px;letter-spacing:14px">QMT</span>
      </div>
      <span class="social" style="left:55px"></span>
      <span class="social" style="left:80px"></span>
      <span class="social" style="left:105px"></span>
      <div class="foot-col" style="left:278px"><h4>Quick Links</h4><ul><li>Home</li><li>About</li><li>Services</li><li>Blog</li><li>contact</li></ul></div>
      <div class="foot-col" style="left:370px"><h4>Contact Us</h4>
        <div class="contact-line"><svg width="6" height="8" viewBox="0 0 6 8"><path d="M3 0a3 3 0 0 1 3 3c0 2-3 5-3 5S0 5 0 3a3 3 0 0 1 3-3z" fill="#f7941d"/></svg><span>Nemo enim ipsam voluptatem quia voluptas sit aspernatur</span></div>
        <div class="contact-line"><svg width="8" height="6" viewBox="0 0 8 6"><rect width="8" height="6" fill="#f7941d"/><path d="M0 0 L4 3 L8 0" stroke="#fff" fill="none" stroke-width=".8"/></svg><span>info@quietmeadowtherapy.com</span></div>
        <div class="contact-line"><svg width="7" height="7" viewBox="0 0 7 7"><path d="M1 0 L2.5 0 L3 2 L2 2.8 Q3 4.5 4.2 5 L5 4 L7 4.5 L7 6 Q6.5 7 5.5 7 Q0 6 0 1 Q0 0 1 0z" fill="#f7941d"/></svg><span>+1 888 888 8888</span></div>
      </div>
    </footer>
    <div class="section copy-bar" style="top:1482px;height:45px">Copyright © 2022, Quiet Meadow Therapy. All rights reserved.</div>
  </main>

</div>
</body>
</html>
```